Company Collaterals

we need the different collaterals to be used for a social media company- we will be including the logo.

Industry/Entity Type

It Company

```html
<!DOCTYPE html>
<html lang="en">
<head>
<meta charset="utf-8">
<title>Kolo Social – Stationery Set</title>
<link href="https://fonts.googleapis.com/css2?family=Open+Sans:wght@400;600;700&display=swap" rel="stylesheet">
<style>
  :root{
    --backdrop:#5e534e;
    --paper:#ffffff;
    --ink:#222222;
    --ink-soft:#555555;
    --card-dark:#303030;
    --purple:#7b3f98;
    --red:#e31e24;
    --orange:#f39323;
    --green:#3f8b3a;
    --blue:#1f8dd6;
  }
  *{box-sizing:border-box;margin:0;padding:0}
  html,body{width:1200px;height:766px;overflow:hidden}
  body{background:var(--backdrop);font-family:"Open Sans",Arial,sans-serif;color:var(--ink);position:relative}

  .sheet{position:absolute;background:var(--paper);box-shadow:0 2px 6px rgba(0,0,0,.35)}
  .letterhead{left:56px;top:64px;width:490px;height:632px}
  .envelope{left:597px;top:175px;width:547px;height:239px}
  .card-front{left:655px;top:469px;width:203px;height:114px}
  .card-back{left:883px;top:469px;width:203px;height:114px;background:var(--card-dark)}

  .brand{position:absolute;display:flex;align-items:center;gap:6px;font-weight:700;color:var(--ink);white-space:nowrap;letter-spacing:.02em}
  .brand-dot{border-radius:50%;background:var(--purple);flex:none}
  .letterhead .brand{left:50%;top:28px;transform:translateX(-50%);font-size:24px}
  .letterhead .brand-dot{width:34px;height:34px}
  .envelope .brand{left:24px;top:26px;font-size:24px}
  .envelope .brand-dot{width:40px;height:40px}
  .card-front .brand{left:11px;top:42px;font-size:12px;gap:4px}
  .card-front .brand-dot{width:20px;height:20px}
  .card-back .brand{left:50%;top:40px;transform:translateX(-50%);font-size:16px;color:#fff;gap:5px}
  .card-back .brand-dot{width:26px;height:26px}

  .contact-footer{position:absolute;left:0;right:0;text-align:center;font-size:8.5px;color:var(--ink)}
  .letterhead .contact-footer{bottom:12px}
  .envelope .contact-footer{bottom:10px}
  .contact-footer .address{margin-bottom:5px}
  .contact-line{display:flex;justify-content:center;gap:7px}
  .contact-item{display:inline-flex;align-items:center;gap:2px}
  .contact-item svg{width:7px;height:7px}

  .color-bar{position:absolute;left:0;right:0;bottom:0;height:5px;display:flex;gap:7px}
  .color-bar span{flex:1}
  .card-front .color-bar{gap:4px}
  .c-purple{background:var(--purple)}
  .c-red{background:var(--red)}
  .c-orange{background:var(--orange)}
  .c-green{background:var(--green)}
  .c-blue{background:var(--blue)}

  .card-details{position:absolute;left:125px;top:19px;font-size:4.6px;line-height:1.45;color:var(--ink-soft)}
  .card-details .person{font-size:6.4px;font-weight:700;color:var(--ink);line-height:1.2}
  .card-details .role{margin-bottom:8px}
  .card-details .address{margin-bottom:2px}
  .card-details .contact-item svg{width:4.5px;height:4.5px}
  .card-details .contact-item{display:flex}

  .card-back .web{position:absolute;left:0;right:0;top:102px;text-align:center;font-size:5px;letter-spacing:.18em;color:#bdbdbd}
</style>
</head>
<body>

<svg width="0" height="0" style="position:absolute" aria-hidden="true">
  <defs>
    <symbol id="ico-phone" viewBox="0 0 10 10"><path d="M2 1l2 2-1 1.2c.6 1.3 1.5 2.2 2.8 2.8L7 6l2 2-1.3 1.3C4.5 9 1 5.5.7 2.3z" fill="var(--blue)"/></symbol>
    <symbol id="ico-mobile" viewBox="0 0 10 10"><rect x="2.5" y=".5" width="5" height="9" rx="1" fill="var(--green)"/><rect x="3.5" y="1.8" width="3" height="5" fill="#fff"/></symbol>
    <symbol id="ico-fax" viewBox="0 0 10 10"><rect x="1" y="4" width="8" height="5" rx="1" fill="var(--orange)"/><rect x="3" y="1" width="4" height="3" fill="var(--orange)"/></symbol>
    <symbol id="ico-mail" viewBox="0 0 10 10"><rect x=".5" y="2" width="9" height="6" fill="var(--red)"/><path d="M.5 2L5 5.5 9.5 2" stroke="#fff" fill="none"/></symbol>
    <symbol id="ico-web" viewBox="0 0 10 10"><circle cx="5" cy="5" r="4.5" fill="var(--purple)"/></symbol>
  </defs>
</svg>

<section class="sheet letterhead">
  <div class="brand"><span class="brand-dot"></span>Kolo Social</div>
  <div class="contact-footer">
    <p class="address">PO BOX 48 Lenford, Arvania</p>
    <div class="contact-line">
      <span class="contact-item"><svg><use href="#ico-phone"/></svg>555-014-220</span>
      <span class="contact-item"><svg><use href="#ico-mobile"/></svg>555-014-220</span>
      <span class="contact-item"><svg><use href="#ico-fax"/></svg>555-014-220</span>
      <span class="contact-item"><svg><use href="#ico-mail"/></svg>info@kolosocial.com</span>
      <span class="contact-item"><svg><use href="#ico-web"/></svg>www.kolosocial.com</span>
    </div>
  </div>
  <div class="color-bar"><span class="c-purple"></span><span class="c-red"></span><span class="c-orange"></span><span class="c-green"></span><span class="c-blue"></span></div>
</section>

<section class="sheet envelope">
  <div class="brand"><span class="brand-dot"></span>Kolo Social</div>
  <div class="contact-footer">
    <p class="address">PO BOX 48 Lenford, Arvania</p>
    <div class="contact-line">
      <span class="contact-item"><svg><use href="#ico-phone"/></svg>555-014-220</span>
      <span class="contact-item"><svg><use href="#ico-mobile"/></svg>555-014-220</span>
      <span class="contact-item"><svg><use href="#ico-fax"/></svg>555-014-220</span>
      <span class="contact-item"><svg><use href="#ico-mail"/></svg>info@kolosocial.com</span>
      <span class="contact-item"><svg><use href="#ico-web"/></svg>www.kolosocial.com</span>
    </div>
  </div>
  <div class="color-bar"><span class="c-purple"></span><span class="c-red"></span><span class="c-orange"></span><span class="c-green"></span><span class="c-blue"></span></div>
</section>

<section class="sheet card-front">
  <div class="brand"><span class="brand-dot"></span>Kolo Social</div>
  <div class="card-details">
    <p class="person">Mara Lind</p>
    <p class="role">Manager</p>
    <p class="address">PO BOX 48 Lenford,<br>Arvania</p>
    <span class="contact-item"><svg><use href="#ico-phone"/></svg>555-014-220</span>
    <span class="contact-item"><svg><use href="#ico-mobile"/></svg>555-014-220</span>
    <span class="contact-item"><svg><use href="#ico-fax"/></svg>555-014-220</span>
    <span class="contact-item"><svg><use href="#ico-mail"/></svg>info@kolosocial.com</span>
    <span class="contact-item"><svg><use href="#ico-web"/></svg>www.kolosocial.com</span>
  </div>
  <div class="color-bar"><span class="c-purple"></span><span class="c-red"></span><span class="c-orange"></span><span class="c-green"></span><span class="c-blue"></span></div>
</section>

<section class="sheet card-back">
  <div class="brand"><span class="brand-dot"></span>Kolo Social</div>
  <p class="web">www.kolosocial.com</p>
</section>

</body>
</html>
```